Animal Horse & Bedding Company Needs a Website Coded & Designed

We need a website for a new animal bedding and feed company that is visually grabbing and vibrant. We would like to see a website that displays trust, quality and confidence. Needs to be responsive and mobile friendly for all browsers and coded for both Android & IOS. SEO is also important.

Joomla or Wordpress – must be both desktop and mobile friendly with fast page load speed. Need the ability to edit ourselves in Wordpress or Joomla.

Full details attached below with some layout and content ideas.

Coding

Coded - Design and coding required

Number of Pages Required

5+ page

Font styles to use
Sans Serif

Requirements
Must have
• Needs to be responsive and mobile friendly for all browsers and coded for both Android & IOS. SEO is also important.

Wordpress – must be both desktop and mobile friendly with fast page load speed. Need the ability to edit ourselves in Wordpress.

Logo Colours:
Dark Brown
CMYK: 50 / 70 / 80 / 70
Pantone: 4625C

Orange
CMYK: 0 / 50 / 100 / 0
Pantone: 144C
Nice to have
• Use picture of building attached and super impose logo on building.

```html
<!DOCTYPE html>
<html lang="en">
<head>
<meta charset="UTF-8">
<title>Harvest Bale – Bedding &amp; Feed</title>
<link href="https://fonts.googleapis.com/css2?family=Oswald:wght@300;400&family=Hind:wght@300;400;500&display=swap" rel="stylesheet">
<style>
:root{
  --brown:#4a2a15;
  --brown-dark:#2e1a0c;
  --orange:#f7941d;
  --page:#e5e5e8;
  --text:#3a2a1e;
  --white:#ffffff;
  --night:#0b1426;
  --black:#050505;
}
*{box-sizing:border-box;margin:0;padding:0}
html,body{width:1200px;height:4187px;overflow:hidden}
body{background:var(--page);font-family:"Hind",Arial,sans-serif;color:var(--text)}
.page{position:relative;width:1200px;height:4187px;overflow:hidden;background:var(--page)}
.abs{position:absolute}

/* header */
.site-header{position:absolute;left:0;top:0;width:1200px;height:91px;background:var(--page);z-index:3}
.brand{position:absolute;left:110px;top:18px;display:flex;align-items:center;gap:10px}
.brand-dot{width:26px;height:26px;border-radius:50%;background:var(--orange)}
.brand-name{font-family:"Oswald",Arial,sans-serif;font-size:30px;color:var(--brown);text-transform:uppercase;letter-spacing:2px;line-height:1}
.nav a{position:absolute;top:40px;font-family:"Oswald",Arial,sans-serif;font-size:20px;color:var(--brown);text-decoration:none;text-transform:uppercase;letter-spacing:1px}
.nav a.active{color:var(--orange)}
.nav-marker{position:absolute;left:474px;top:20px;width:10px;height:12px;border-radius:50%;background:var(--orange)}
.quote-btn{position:absolute;right:0;top:0;width:190px;height:91px;background:var(--orange);color:var(--white);font-family:"Oswald",Arial,sans-serif;font-size:26px;text-transform:uppercase;display:flex;align-items:center;justify-content:center;letter-spacing:1px}

/* hero */
.hero{position:absolute;left:0;top:91px;width:1200px;height:680px}
.hero-title{position:absolute;left:0;top:200px;width:1200px;text-align:center;font-family:"Oswald",Arial,sans-serif;font-weight:300;font-size:108px;color:var(--white);letter-spacing:4px;line-height:1.1;text-transform:uppercase}
.hero-arrow{position:absolute;top:246px;width:66px;height:66px;border:2px solid var(--white);border-radius:50%}
.hero-dots{position:absolute;left:574px;top:596px;display:flex;gap:10px;align-items:center}
.hero-dots span{width:6px;height:6px;border-radius:50%;background:var(--white)}
.hero-dots span.on{width:12px;height:12px;background:var(--orange);border:2px solid #f9c27a}

/* body text */
.lead{position:absolute;left:172px;width:856px;text-align:center;font-size:18px;line-height:30px;color:var(--text)}
.rule{position:absolute;left:110px;top:1163px;width:980px;height:1px;background:#b9b3ae}
.rule-badge{position:absolute;left:570px;top:1133px;width:60px;height:60px;border-radius:50%;background:var(--brown);border:5px solid var(--white);box-shadow:0 0 0 1px #c9c3be}

.section-title{position:absolute;left:0;width:1200px;text-align:center;font-family:"Oswald",Arial,sans-serif;font-weight:300;font-size:50px;color:var(--brown);letter-spacing:2px;text-transform:uppercase}
.section-title .accent{color:var(--orange)}
.ornament{position:absolute;width:134px;height:20px}
.ornament::before,.ornament::after{content:"";position:absolute;top:9px;width:50px;height:2px;background:var(--orange)}
.ornament::before{left:0}.ornament::after{right:0}
.ornament i{position:absolute;left:59px;top:0;width:16px;height:20px;border-radius:50%;border:2px solid var(--orange)}

/* offer cards */
.card{position:absolute;top:1473px;width:292px;height:288px;background:var(--white);border:2px solid #f7b466;border-radius:14px;text-align:center}
.card svg{position:absolute;left:116px;top:22px}
.card h3{position:absolute;left:0;top:138px;width:100%;font-family:"Oswald",Arial,sans-serif;font-weight:400;font-size:20px;color:var(--orange);letter-spacing:.5px;text-transform:uppercase;white-space:nowrap}
.card p{position:absolute;left:40px;top:186px;width:212px;font-size:16px;line-height:28px;color:#6b5e56}

/* bedding */
.bedding-band{position:absolute;left:0;top:1894px;width:600px;height:553px;background:linear-gradient(120deg,#9f958c 0%,#cbc3ba 45%,#dcd6cf 100%)}
.bedding-band::after{content:"";position:absolute;inset:0;background:rgba(229,229,232,.55)}
.bedding-photo{position:absolute;left:553px;top:1850px;width:647px;height:641px;background:linear-gradient(160deg,#98a86f 0%,#6f6548 40%,#5a4030 70%,#7a5a44 100%);clip-path:polygon(70px 0,647px 0,647px 641px,0 641px,10px 450px,30px 200px)}
.ticks{position:absolute;list-style:none}
.ticks li{position:relative;padding-left:36px;font-size:16px;line-height:22px;color:var(--text)}
.ticks li::before{content:"";position:absolute;left:2px;top:6px;width:8px;height:8px;border-radius:50%;background:var(--brown-dark)}
.btn-outline{position:absolute;height:52px;border-radius:26px;background:var(--orange);border:3px solid var(--page);box-shadow:0 0 0 2px var(--orange);color:var(--white);font-family:"Oswald",Arial,sans-serif;font-size:20px;display:flex;align-items:center;justify-content:center;text-transform:uppercase;letter-spacing:1px}
.left-title{position:absolute;font-family:"Oswald",Arial,sans-serif;font-weight:300;font-size:48px;color:var(--brown);letter-spacing:2px;text-transform:uppercase}

/* feed */
.feed-ring{position:absolute;left:165px;top:2792px;width:464px;height:464px;border-radius:50%;border:2px solid #9c948e}
.feed-photo{position:absolute;left:180px;top:2807px;width:434px;height:434px;border-radius:50%;background:radial-gradient(circle at 50% 45%,#e9e4dc 0%,#c9a868 45%,#9c7a3c 100%)}
.sub-title{position:absolute;font-family:"Oswald",Arial,sans-serif;font-weight:400;font-size:26px;color:var(--brown);letter-spacing:1px;text-transform:uppercase}

/* delivery */
.delivery{position:absolute;left:0;top:3382px;width:1200px;height:420px;background:radial-gradient(ellipse at 50% 110%,#36466a 0%,#142342 45%,#070d1c 100%)}
.delivery-title{position:absolute;left:0;top:3470px;width:1200px;text-align:center;font-family:"Oswald",Arial,sans-serif;font-weight:300;font-size:72px;color:var(--white);letter-spacing:3px;text-transform:uppercase}
.delivery-title span{color:var(--orange)}

/* footer */
.site-footer{position:absolute;left:0;top:3740px;width:1200px;height:447px;background:var(--black)}
.foot-brand{position:absolute;left:110px;top:3860px;display:flex;align-items:center;gap:12px}
.foot-brand .brand-name{color:var(--white);font-size:36px}
.social{position:absolute;top:3976px;width:64px;height:64px;border-radius:50%;border:2px solid var(--white);display:flex;align-items:center;justify-content:center}
.foot-col h4{position:absolute;font-family:"Oswald",Arial,sans-serif;font-weight:400;font-size:16px;color:var(--white);letter-spacing:1px;text-transform:uppercase}
.foot-link{position:absolute;font-size:12px;color:#e6e6e6}
.foot-copy{position:absolute;font-size:12px;line-height:20px;color:#e6e6e6}
.mail-input{position:absolute;left:748px;top:3966px;width:340px;height:44px;border-radius:22px;background:var(--white);padding-left:30px;font-size:13px;color:#999;display:flex;align-items:center}
.submit{position:absolute;left:750px;top:4032px;width:115px;height:40px;border-radius:20px;background:var(--orange);border:3px solid var(--black);box-shadow:0 0 0 2px var(--orange);color:var(--white);font-family:"Oswald",Arial,sans-serif;font-size:17px;display:flex;align-items:center;justify-content:center;text-transform:uppercase}
.foot-rule{position:absolute;left:110px;top:4111px;width:980px;height:1px;background:#5a3d22}
.legal-sep{position:absolute;left:1011px;top:4122px;width:1px;height:30px;background:#ccc}
</style>
</head>
<body>
<div class="page">

  <header class="site-header">
    <div class="brand"><span class="brand-dot"></span><span class="brand-name">Harvest Bale</span></div>
    <nav class="nav">
      <span class="nav-marker"></span>
      <a class="active" style="left:457px">Home</a>
      <a style="left:556px">About</a>
      <a style="left:660px">Feed</a>
      <a style="left:756px">Bedding</a>
      <a style="left:878px">Contact Us</a>
    </nav>
    <div class="quote-btn">Request Quote</div>
  </header>

  <section class="hero">
    <svg class="abs" style="left:0;top:0" width="1200" height="680" viewBox="0 0 1200 680">
      <defs>
        <linearGradient id="heroSky" x1="0" y1="0" x2="0" y2="1">
          <stop offset="0" stop-color="#8fb6dc"/>
          <stop offset="0.35" stop-color="#d7e2ea"/>
          <stop offset="0.45" stop-color="#6f8a55"/>
          <stop offset="0.65" stop-color="#9a3a33"/>
          <stop offset="0.85" stop-color="#6a6455"/>
          <stop offset="1" stop-color="#5d5a4c"/>
        </linearGradient>
      </defs>
      <path role="img" aria-label="Aerial photo of a red-roofed stable and barn complex surrounded by paddocks and fields" d="M0 0H1200V560Q600 740 0 560Z" fill="url(#heroSky)"/>
      <path d="M0 560Q600 770 1200 560V600Q600 790 0 600Z" fill="var(--orange)"/>
      <path d="M0 600Q600 790 1200 600" fill="none" stroke="var(--brown)" stroke-width="3"/>
      <path d="M0 603Q600 800 1200 603V680H0Z" fill="var(--page)"/>
    </svg>
    <h1 class="hero-title">Harvest Bale</h1>
    <div class="hero-arrow" style="left:18px">
      <svg width="62" height="62" viewBox="0 0 62 62"><path d="M35 21L25 31L35 41" fill="none" stroke="#fff" stroke-width="3"/></svg>
    </div>
    <div class="hero-arrow" style="left:1116px">
      <svg width="62" height="62" viewBox="0 0 62 62"><path d="M27 21L37 31L27 41" fill="none" stroke="#fff" stroke-width="3"/></svg>
    </div>
    <div class="hero-dots"><span class="on"></span><span></span><span></span><span></span></div>
  </section>

  <p class="lead" style="top:860px">Looking for the best bedding and feed for your horse, livestock or household pet look no further.&nbsp; We use premium locally sourced straw and hay in all of our products and are committed in providing quality products and service.</p>
  <p class="lead" style="top:980px">Your animal deserves the very best in health and comfort to keep them healthy, strong and happy.&nbsp; Our products are designed for horses, livestock (goats, cattle and sheep), small caged animals (rabbits, guinea pigs and more).</p>

  <div class="rule"></div>
  <div class="rule-badge"></div>

  <h2 class="section-title" style="top:1236px">Our <span class="accent">Offer</span></h2>
  <div class="ornament" style="left:533px;top:1298px"><i></i></div>
  <p class="lead" style="top:1334px">Harvest Bale offers supply and delivery of fresh bedding as well as removal of waste bedding.&nbsp; Let us deliver you a container of fresh straw and haul your waste bedding away.&nbsp; A full service solution that is sustainable and responsible.</p>

  <div class="card" style="left:110px">
    <svg width="60" height="80" viewBox="0 0 60 80">
      <path d="M30 4L54 14V40Q54 62 30 76Q6 62 6 40V14Z" fill="none" stroke="var(--brown)" stroke-width="3"/>
      <path d="M30 14L46 21V40Q46 56 30 66Q14 56 14 40V21Z" fill="none" stroke="var(--brown)" stroke-width="2"/>
      <circle cx="30" cy="40" r="11" fill="none" stroke="var(--orange)" stroke-width="2.5"/>
      <path d="M24 40L29 45L37 35" fill="none" stroke="var(--orange)" stroke-width="2.5"/>
    </svg>
    <h3>Quality Guaranteed</h3>
    <p>Grown for quality - 100% natural with no chemicals or additives</p>
  </div>
  <div class="card" style="left:454px">
    <svg width="86" height="80" viewBox="0 0 86 80">
      <rect x="4" y="22" width="62" height="46" fill="none" stroke="var(--brown)" stroke-width="3"/>
      <path d="M4 22L35 48L66 22M4 68L28 44M66 68L42 44" fill="none" stroke="var(--brown)" stroke-width="2.5"/>
      <circle cx="66" cy="18" r="14" fill="#fff" stroke="var(--orange)" stroke-width="2.5"/>
      <text x="66" y="23" text-anchor="middle" font-family="Hind,sans-serif" font-size="13" font-weight="500" fill="var(--brown)">24</text>
    </svg>
    <h3>Full Service Solution</h3>
    <p>Dedicated in providing a full service solution of bedding supply &amp; waste removal</p>
  </div>
  <div class="card" style="left:792px">
    <svg width="76" height="80" viewBox="0 0 76 80">
      <g fill="none" stroke="var(--brown)" stroke-width="2.5">
        <rect x="4" y="54" width="12" height="18"/><rect x="20" y="46" width="12" height="26"/>
        <rect x="36" y="38" width="12" height="34"/><rect x="52" y="30" width="12" height="42"/>
      </g>
      <path d="M6 44L24 34L40 28L62 10M52 10H62V20" fill="none" stroke="var(--orange)" stroke-width="2.5"/>
    </svg>
    <h3>Convenient &amp; Cost Effective</h3>
    <p>Compressed bags , pellets or bulk products saving in shipping costs</p>
  </div>

  <div class="bedding-band" role="img" aria-label="Soft photo of a horse standing in straw bedding"></div>
  <div class="bedding-photo" role="img" aria-label="Photo of a brown rabbit sitting on mulch bedding outdoors"></div>
  <h2 class="left-title" style="left:110px;top:1920px">Bedding</h2>
  <div class="ornament" style="left:110px;top:1984px"><i></i></div>
  <ul class="ticks" style="left:110px;top:2040px">
    <li style="margin-bottom:19px">100% Natural Chopped Straw</li>
    <li style="margin-bottom:19px">Low Dust</li>
    <li style="margin-bottom:19px">Chemical &amp; Additive Free</li>
    <li style="margin-bottom:19px">Clean &amp; Highly Absorbent</li>
    <li style="margin-bottom:19px">Cheaper than Wood Shavings</li>
    <li style="margin-bottom:19px">Economic – less used and less wasted</li>
    <li>Environmentally Friendly –<br>Recyclable &amp; Compostable</li>
  </ul>
  <div class="btn-outline" style="left:112px;top:2358px;width:194px">Learn More</div>

  <h2 class="section-title" style="top:2566px">Feed</h2>
  <div class="ornament" style="left:533px;top:2626px"><i></i></div>
  <p class="lead" style="left:155px;width:890px;top:2670px">Hay cubes and pellets are made from premium hay offering a variety of animals a feed that is non-GMO and packed with natural nutrients.&nbsp; These pellets and cubes are less bulky to handle, store and ship. As well, they reduce the amount of wasted feed.</p>

  <div class="feed-ring"></div>
  <div class="feed-photo" role="img" aria-label="Photo of a young goat standing on golden straw"></div>

  <h3 class="sub-title" style="left:748px;top:2780px">Benefits</h3>
  <ul class="ticks" style="left:748px;top:2836px">
    <li style="margin-bottom:18px">100% Natural</li>
    <li style="margin-bottom:18px">Chemical &amp; Additive Free</li>
    <li style="margin-bottom:18px">Available in Pellets or Cubes</li>
    <li style="margin-bottom:18px">High Protein Content</li>
    <li style="margin-bottom:18px">Eliminate Waste In Feeding</li>
    <li style="margin-bottom:18px">Clean - Eliminates Dust From<br>Feeding Baled Hay</li>
    <li style="margin-bottom:18px">Cost Effective</li>
    <li style="margin-bottom:18px">Convenient</li>
    <li>Less wasted feed</li>
  </ul>
  <div class="btn-outline" style="left:752px;top:3242px;width:190px">Learn More</div>

  <div class="delivery" role="img" aria-label="Night view of the earth with glowing network lines across North America"></div>
  <h2 class="delivery-title">Delivery in <span>Canada</span> &amp; <span>USA</span></h2>

  <footer class="site-footer"></footer>
  <svg class="abs" style="left:0;top:3700px" width="1200" height="110" viewBox="0 0 1200 110">
    <path d="M0 90Q600 -20 1200 90V110H0Z" fill="var(--black)"/>
    <path d="M0 90Q600 -20 1200 90V70Q600 -44 0 70Z" fill="var(--orange)"/>
  </svg>

  <div class="foot-brand"><span class="brand-dot" style="width:32px;height:32px"></span><span class="brand-name">Harvest Bale</span></div>

  <div class="social" style="left:127px">
    <svg width="26" height="26" viewBox="0 0 24 24"><path d="M6.6 10.8a15 15 0 0 0 6.6 6.6l2.2-2.2a1 1 0 0 1 1-.25 11.4 11.4 0 0 0 3.6.57 1 1 0 0 1 1 1V20a1 1 0 0 1-1 1A17 17 0 0 1 3 4a1 1 0 0 1 1-1h3.5a1 1 0 0 1 1 1c0 1.25.2 2.45.57 3.57a1 1 0 0 1-.25 1z" fill="var(--orange)"/></svg>
  </div>
  <div class="social" style="left:205px">
    <svg width="28" height="22" viewBox="0 0 28 22"><rect x="2" y="2" width="24" height="18" rx="2" fill="none" stroke="var(--orange)" stroke-width="2.5"/><path d="M3 4L14 12L25 4" fill="none" stroke="var(--orange)" stroke-width="2.5"/></svg>
  </div>
  <div class="social" style="left:283px">
    <svg width="26" height="26" viewBox="0 0 26 26"><circle cx="13" cy="13" r="10" fill="none" stroke="var(--orange)" stroke-width="2.5"/><path d="M3 13H23M13 3Q7 13 13 23M13 3Q19 13 13 23" fill="none" stroke="var(--orange)" stroke-width="2"/></svg>
  </div>

  <div class="foot-col">
    <h4 style="left:429px;top:3856px">Quick Links</h4>
    <span class="foot-link" style="left:429px;top:3896px">Home</span>
    <span class="foot-link" style="left:429px;top:3923px">About</span>
    <span class="foot-link" style="left:429px;top:3950px">Feed</span>
    <span class="foot-link" style="left:429px;top:3977px">Bedding</span>
    <span class="foot-link" style="left:429px;top:4004px">Contact US</span>

    <h4 style="left:576px;top:3856px">Links</h4>
    <span class="foot-link" style="left:576px;top:3896px">Terms &amp; Condition</span>
    <span class="foot-link" style="left:576px;top:3923px">Privacy Policy</span>
    <span class="foot-link" style="left:576px;top:3950px">Sitemap</span>

    <h4 style="left:748px;top:3856px">Get Our Latest Updates</h4>
    <p class="foot-copy" style="left:748px;top:3892px;width:300px;line-height:25px">Enter your mail and we'll send you all uptodate latest blog and news</p>
  </div>
  <div class="mail-input">Enter your mail</div>
  <div class="submit">Submit</div>

  <div class="foot-rule"></div>
  <span class="foot-link" style="left:110px;top:4136px">Copyrights ©2021 Harvest Bale. All Rights Reserved</span>
  <span class="foot-link" style="left:899px;top:4136px">Privacy Policy</span>
  <div class="legal-sep"></div>
  <span class="foot-link" style="left:1034px;top:4136px">Sitemap</span>

</div>
</body>
</html>
```